Pet business needs a business card

Pet shop needs a business card. Like dark background and and debased look.

Meadowpaws
Lindenweg 47
B - 3280 Velmor
Belgium

www.meadowpaws-example.com
mail@meadowpaws-example.com
Phone +32478610927

I will ad a tagline shortly.

Industry/Entity Type

Shop

Font styles to use
Sans Serif

Requirements
Must have
• Must be possible to print the card debased. See example image.

```html
<!DOCTYPE html>
<html lang="en">
<head>
<meta charset="utf-8">
<title>Meadowpaws – Business Card</title>
<link rel="stylesheet" href="https://fonts.googleapis.com/css2?family=Open+Sans:wght@400;700;800&display=swap">
<style>
  :root {
    --backdrop: #2b2b30;
    --card: #36363d;
    --amber: #e6a146;
    --olive: #8b8a74;
    --ink-muted: #77766f;
    --phone-ink: #6e6a63;
  }
  * { margin: 0; padding: 0; box-sizing: border-box; }
  html, body {
    width: 1200px; height: 800px; overflow: hidden;
    background: var(--backdrop);
    font-family: "Open Sans", Arial, sans-serif;
  }
  .sheet {
    position: relative; width: 1200px; height: 800px;
    display: flex; align-items: center; justify-content: center; gap: 40px;
  }
  .card {
    position: relative; width: 520px; height: 300px;
    background: var(--card); overflow: hidden;
    box-shadow: 0 10px 30px rgba(0,0,0,.35);
  }
  /* Contact side */
  .sail { position: absolute; inset: 0; width: 520px; height: 300px; }
  .brand-name {
    position: absolute; left: 36px; top: 92px;
    font-size: 34px; font-weight: 800; letter-spacing: 0.5px;
    color: var(--olive);
  }
  .address {
    position: absolute; left: 38px; top: 170px;
    font-size: 11.5px; line-height: 19px; color: var(--ink-muted);
    font-style: normal;
  }
  .web {
    position: absolute; left: 38px; top: 252px;
    font-size: 11px; line-height: 15px; color: var(--ink-muted);
  }
  .phone {
    position: absolute; right: 26px; top: 98px;
    color: var(--phone-ink); line-height: 1.2;
    text-align: center; white-space: nowrap;
  }
  .phone-label { font-size: 19px; }
  .phone-number { font-size: 21px; letter-spacing: 0.5px; }
  /* Logo side */
  .mascot-area {
    position: absolute; left: 140px; top: 36px; width: 300px; height: 170px;
    background: linear-gradient(135deg, var(--amber) 0%, var(--amber) 60%, var(--olive) 100%);
    border-radius: 6px; opacity: .9;
  }
  .logo-name {
    position: absolute; left: 0; right: 0; top: 216px; text-align: center;
    font-size: 38px; font-weight: 800; letter-spacing: 0.5px;
    color: var(--amber);
  }
</style>
</head>
<body>
  <main class="sheet">
    <section class="card card--contact">
      <svg class="sail" viewBox="0 0 520 300" aria-hidden="true">
        <path d="M 430 0 L 520 0 L 520 300 L 245 300 C 255 200 330 90 430 0 Z" fill="var(--amber)"/>
      </svg>
      <div class="brand-name">Meadowpaws</div>
      <address class="address">Lindenweg 47<br>B - 3280 Velmor<br>Belgium</address>
      <div class="web">www.meadowpaws-example.com<br>mail@meadowpaws-example.com</div>
      <div class="phone">
        <div class="phone-label">Phone:</div>
        <div class="phone-number">+32478610927</div>
      </div>
    </section>

    <section class="card card--logo">
      <div class="mascot-area" role="img" aria-label="Illustration of a walking long-eared dog in amber and olive"></div>
      <div class="logo-name">Meadowpaws</div>
    </section>
  </main>
</body>
</html>
```